Catalogue Design Project

We require a new 2013 catalogue cover designed ( front & back with a one inch wide spine) for our business, Brellock Office Supplies. We have been established for 36 years and we supply all sorts of companies across the UK with a Variety of Office Stationery, Computer Products, Print, Furniture, Catering and Cleaning products within the UK - you can browse our catalogue on our website www.brellock.co.uk - using test as both user id and password.
We are serious about customer service; ensure we do the very best for our clients with the best prices. For us it’s all about the image we portray to our clients, we don’t want the cover to look like it’s the cover of a Yacht catalogue, nor do we want it to look like a trashy magazine.
The main priority of this design is that the Catalogue looks professional and appealing. Good use of colour, possibly incorporating elements of what we do would be of advantage.
(Please visit our website www.brellock.co.uk for details).
The Catalogue is to be A4 in size, MUST have our company logo in on the front, which we will supply, but for the start obtainable from our site)
The Catalogue covers will have insides both front and back that we will be printing on. Your design and use of colours should be able to flow onto these pages so as we can print on a continuation of your design.
**UPDATE - Please note the content is already designed, this is for the front/back cover and inside covers**
There will be a few edits after we make a choice...
if you need anything from us then please email us on jpoll@brellock.co.uk
Best of luck
Reason: Deaedline Extended to give you all a chance to get your designs in!!
Reason: Having some great creative ideas in, so herew is a chance for one last push before we make our decision.
PROJECT NOW GUARANTEED.!!
Due to the High Quality of designs being submitted - we are now happy to commit to one of you! Keep the designs coming!
Good Luck!
Target Market(s)
The Buyers of our products are corporate companies
Industry/Entity Type
Printing
Look and feel

```html
<!DOCTYPE html>
<html lang="en">
<head>
<meta charset="utf-8">
<title>Brellock Office Supplies – 2013 Catalogue Cover</title>
<link rel="stylesheet" href="https://fonts.googleapis.com/css2?family=Roboto+Condensed:wght@700&family=Roboto:wght@400;500&display=swap">
<style>
  :root {
    --backdrop: #4a4a4a;
    --cover-yellow: #f2d52a;
    --spine-yellow: #eec81c;
    --band-yellow: #f6e27a;
    --band-pale: #f8eaa6;
    --paper-grey: #ebebea;
    --logo-grey: #a9a9a9;
    --white: #ffffff;
    --url-yellow: #e8c21a;
  }
  html, body {
    margin: 0;
    padding: 0;
    width: 1200px;
    height: 1000px;
    overflow: hidden;
    background: var(--backdrop);
  }
  .canvas {
    position: relative;
    width: 1200px;
    height: 1000px;
    display: flex;
    align-items: center;
    justify-content: center;
  }
  .cover-spread {
    display: block;
    width: 1100px;
    height: 373px;
  }
  .title-year { font-family: "Roboto Condensed", sans-serif; font-weight: 700; fill: var(--white); }
  .title-word { font-family: "Roboto", sans-serif; font-weight: 500; fill: var(--white); letter-spacing: 1px; }
  .brand-name { font-family: "Roboto", sans-serif; font-weight: 400; fill: var(--logo-grey); letter-spacing: 3px; }
  .brand-name--light { fill: var(--white); }
  .spine-title { font-family: "Roboto Condensed", sans-serif; font-weight: 700; fill: var(--white); }
  .web-address { font-family: "Roboto", sans-serif; font-weight: 500; fill: var(--url-yellow); letter-spacing: 1.5px; }
</style>
</head>
<body>
<main class="canvas">
  <svg class="cover-spread" viewBox="0 0 978 332" xmlns="http://www.w3.org/2000/svg" aria-label="Brellock Office Supplies 2013 catalogue cover spread">
    <!-- Back cover -->
    <g class="back-cover">
      <rect x="0" y="0" width="468" height="332" fill="var(--cover-yellow)"/>
      <path d="M0 185 C120 205 300 250 440 332 L0 332 Z" fill="var(--band-pale)"/>
      <path d="M0 198 C140 215 310 258 420 332 L0 332 Z" fill="var(--band-yellow)" opacity="0.6"/>
      <path d="M0 212 C150 230 300 270 395 332 L0 332 Z" fill="var(--paper-grey)"/>
      <rect x="190" y="98" width="9" height="9" fill="var(--white)"/>
      <text class="brand-name brand-name--light" x="204" y="107" font-size="13">BRELLOCK</text>
      <text class="brand-name brand-name--light" x="205" y="117" font-size="6" letter-spacing="0.5">Office Supplies</text>
      <text class="title-year" x="186" y="165" font-size="42">2013</text>
      <text class="title-word" x="188" y="184" font-size="15">Catalogue</text>
      <text class="web-address" x="28" y="316" font-size="12">www.brellock.co.uk</text>
    </g>

    <!-- Spine -->
    <g class="spine">
      <rect x="468" y="0" width="42" height="332" fill="var(--spine-yellow)"/>
      <line x1="469.5" y1="0" x2="469.5" y2="332" stroke="var(--white)" stroke-width="1.5"/>
      <line x1="508.5" y1="0" x2="508.5" y2="332" stroke="var(--white)" stroke-width="1.5"/>
      <text class="spine-title" transform="translate(484 18) rotate(90)" font-size="10">2013 Catalogue</text>
      <text class="brand-name brand-name--light" transform="translate(486 215) rotate(90)" font-size="11">BRELLOCK</text>
      <text class="brand-name brand-name--light" transform="translate(477 215) rotate(90)" font-size="5" letter-spacing="0.5">Office Supplies</text>
    </g>

    <!-- Front cover -->
    <g class="front-cover">
      <rect x="510" y="0" width="468" height="332" fill="var(--cover-yellow)"/>
      <path d="M652 100 L722 0 L978 0 L978 300 C880 230 760 150 652 100 Z"
            fill="url(#productGradient)" role="img"
            aria-label="Collage of office stationery products: pens, sticky notes, tape, paper clips and pencils"/>
      <path d="M510 332 C640 250 820 205 978 200 L978 332 Z" fill="var(--band-pale)"/>
      <path d="M540 332 C660 262 830 225 978 222 L978 332 Z" fill="var(--band-yellow)" opacity="0.6"/>
      <path d="M570 332 C690 275 840 245 978 245 L978 332 Z" fill="var(--paper-grey)"/>
      <text class="title-year" x="538" y="134" font-size="42">2013</text>
      <text class="title-word" x="544" y="151" font-size="15">Catalogue</text>
      <rect x="786" y="292" width="10" height="10" fill="var(--logo-grey)"/>
      <text class="brand-name" x="800" y="304" font-size="18">BRELLOCK</text>
      <text class="brand-name" x="832" y="316" font-size="8" letter-spacing="0.5">Office Supplies</text>
    </g>

    <defs>
      <linearGradient id="productGradient" x1="0" y1="0" x2="1" y2="1">
        <stop offset="0" stop-color="#3f6fb5"/>
        <stop offset="0.35" stop-color="#6d8fc4"/>
        <stop offset="0.6" stop-color="#c9a45a"/>
        <stop offset="1" stop-color="#e6c93a"/>
      </linearGradient>
    </defs>
  </svg>
</main>
</body>
</html>
```